Need Letterhead & Stationery for Construction Company

Hello,
I have a small construction company that I recently started. I already have the logo but I want to create a letterhead, stationery and business cards for it. I want an elegant design which should feel like a corporate company. Kindly let me know what else you need from my end to start with the design.
I also need digital copies of letterhead so that I can send PDF's directly to clients.

** logo attached, colors I would like to stay in Grey / Shades of Red

** Details required in Business Card:
Name, Designation, Mobile, Telephone, Email, other email, POBOX, Address, website

Requirements
Should not have
• funky styles, too many colors.

```html
<!DOCTYPE html>
<html lang="en">
<head>
<meta charset="utf-8">
<title>Halvorsen Steel Works – Letterhead</title>
<link href="https://fonts.googleapis.com/css2?family=Montserrat:wght@500&family=Roboto:wght@300;400;700&family=Great+Vibes&display=swap" rel="stylesheet">
<style>
  :root {
    --red: #ec1c33;
    --red-deep: #bb1f2a;
    --ink: #111111;
    --text: #555555;
    --text-dark: #333333;
    --icon-dark: #1f2a33;
    --backdrop: #ececec;
    --paper: #ffffff;
  }
  html, body {
    margin: 0;
    width: 1200px;
    height: 1200px;
    overflow: hidden;
    background: var(--backdrop);
  }
  .letterhead {
    position: absolute;
    left: 196px;
    top: 30px;
    width: 963px;
    height: 1356px;
    background: var(--paper);
    transform: scale(0.84);
    transform-origin: top left;
    box-shadow: 0 6px 24px rgba(0,0,0,0.12);
    font-family: "Roboto", Arial, sans-serif;
    overflow: hidden;
  }
  .corner-art {
    position: absolute;
    display: block;
  }
  .corner-art.top { right: 0; top: 0; width: 483px; height: 326px; }
  .corner-art.bottom { left: 0; bottom: 0; width: 485px; height: 224px; }
  .brand {
    position: absolute;
    left: 55px;
    top: 74px;
    display: flex;
    align-items: center;
    gap: 22px;
  }
  .brand-dot {
    width: 78px;
    height: 78px;
    border-radius: 50%;
    background: var(--ink);
  }
  .brand-name {
    font-family: "Montserrat", Arial, sans-serif;
    font-weight: 500;
    color: var(--ink);
    line-height: 1;
  }
  .brand-name .main {
    display: block;
    font-size: 50px;
    letter-spacing: 4px;
  }
  .brand-name .sub {
    display: block;
    font-size: 13px;
    letter-spacing: 0.3px;
    margin-top: 8px;
  }
  .recipient {
    position: absolute;
    left: 44px;
    top: 304px;
    font-style: normal;
    font-size: 16px;
    font-weight: 300;
    color: var(--text-dark);
    line-height: 22px;
  }
  .recipient .name,
  .recipient .company {
    color: var(--red);
    font-weight: 700;
    font-size: 15.5px;
  }
  .recipient .company { margin-top: 4px; display: block; }
  .date {
    position: absolute;
    right: 64px;
    top: 380px;
    font-size: 15px;
    font-weight: 300;
    color: var(--text-dark);
  }
  .date b { color: var(--red); font-weight: 700; }
  .body-copy {
    position: absolute;
    left: 44px;
    top: 516px;
    width: 869px;
    font-size: 16.6px;
    line-height: 20.8px;
    color: var(--text);
    text-align: justify;
  }
  .body-copy p {
    margin: 0 0 20.8px;
    text-indent: 172px;
  }
  .signoff {
    position: absolute;
    left: 50px;
    top: 992px;
  }
  .signoff .signature {
    font-family: "Great Vibes", cursive;
    color: var(--red);
    font-size: 32px;
    line-height: 36px;
  }
  .signoff .name {
    font-size: 19px;
    font-weight: 400;
    color: var(--ink);
    margin-top: 4px;
  }
  .signoff .role {
    font-size: 15.5px;
    font-weight: 700;
    color: var(--red);
  }
  .contacts {
    position: absolute;
    right: 50px;
    top: 1190px;
    list-style: none;
    margin: 0;
    padding: 0;
  }
  .contacts li {
    display: flex;
    justify-content: flex-end;
    align-items: center;
    gap: 13px;
    margin-bottom: 10px;
  }
  .contacts .lines {
    text-align: right;
    font-size: 12.5px;
    line-height: 15.5px;
    color: var(--text-dark);
  }
  .contacts .icon {
    width: 26px;
    height: 26px;
    display: block;
  }
</style>
</head>
<body>
<main class="letterhead">
  <svg class="corner-art top" viewBox="0 0 483 326" role="img" aria-label="Decorative red corner artwork">
    <defs>
      <linearGradient id="cornerTop" x1="0" y1="0" x2="1" y2="1">
        <stop offset="0" stop-color="#bb1f2a"/>
        <stop offset="1" stop-color="#ec1c33"/>
      </linearGradient>
    </defs>
    <polygon points="0,0 483,0 483,326" fill="url(#cornerTop)"/>
  </svg>

  <svg class="corner-art bottom" viewBox="0 0 485 224" role="img" aria-label="Decorative red corner artwork">
    <defs>
      <linearGradient id="cornerBottom" x1="0" y1="0" x2="1" y2="1">
        <stop offset="0" stop-color="#ec1c33"/>
        <stop offset="1" stop-color="#bb1f2a"/>
      </linearGradient>
    </defs>
    <polygon points="0,0 485,224 0,224" fill="url(#cornerBottom)"/>
  </svg>

  <header class="brand">
    <span class="brand-dot"></span>
    <span class="brand-name">
      <span class="main">HALVORSEN</span>
      <span class="sub">STEEL WORKS LLC</span>
    </span>
  </header>

  <address class="recipient">
    To<br>
    <span class="name">Daniel Reyes</span><br>
    Chief Executive Officer<br>
    <span class="company">Northgate Partners LLC</span>
    48 Alder Lane,<br>
    CA, USA 904215
  </address>

  <div class="date"><b>Date:</b> 24-03-2018</div>

  <section class="body-copy">
    <p>Lorem ipsum dolor sit amet, consectetur adipiscing elit. Pellentesque dictum, ante non ullamcorp er convallis, nunc quam blandit metus, ac mollis eros felis a orci. Donec congue, mauris ut pulvinar lobortis, dolor massa feugiat nisi, at tincidunt metus leo vel elit.</p>
    <p>Nulla egestas vulputate risus, ut vestibulum diam commodo id. Mauris ornare libero eu erat portt itor ultrices. Proin sed lectus scelerisque ligula bibendum sagittis ac nec leo. Donec ac accumsan diam, et lobortis mauris. Nulla congue volutpat nisl ac lobortis. Integer dignissim interdum libero, quis feugiat velit pretium at. Phasellus sit amet libero rutrum, feugiat odio et, tempus purus. Cras ultricies, leo at fringilla solli cit udin, leo sapien placerat enim, a rutrum lorem enim ut tortor. Phasellus magna ante, cong ue maximus egestas sit amet, venenatis scelerisque felis.</p>
    <p>Nulla congue volutpat nisl ac lobortis. Integer dignissim interdum libero, quis feugiat velit pretium at. Phasellus sit amet libero rutrum, feugiat odio et, tempus purus. Cras ultricies, leo at fringilla solli cit udin, leo sapien placerat enim, a rutrum lorem enim ut tortor. Phasellus magna ante, cong ue maximus egestas sit amet, venenatis scelerisque felis.</p>
    <p>Nulla congue volutpat nisl ac lobortis. Integer dignissim interdum libero, quis feugiat velit pretium at. Phasellus sit amet libero rutrum, feugiat odio et, tempus purus. Cras ultricies, leo at fringilla solli cit udin, leo sapien placerat enim, a rutrum lorem enim ut tortor. Phasellus magna ante, cong ue maximus egestas sit amet, venenatis scelerisque felis</p>
  </section>

  <div class="signoff">
    <div class="signature">Aaron Blake</div>
    <div class="name">AARON BLAKE</div>
    <div class="role">Chief Finance Officer</div>
  </div>

  <ul class="contacts">
    <li>
      <span class="lines">+1 555 0142 7731<br>+1 555 0198 2640</span>
      <svg class="icon" viewBox="0 0 26 26" aria-hidden="true">
        <rect width="26" height="26" fill="var(--red)"/>
        <rect x="9.5" y="6" width="7" height="13" rx="1.2" fill="none" stroke="#fff" stroke-width="1.6"/>
        <circle cx="13" cy="16.6" r="0.9" fill="#fff"/>
      </svg>
    </li>
    <li>
      <span class="lines">office@halvorsensteel.com<br>www.halvorsensteel.com</span>
      <svg class="icon" viewBox="0 0 26 26" aria-hidden="true">
        <rect width="26" height="26" fill="var(--icon-dark)"/>
        <g fill="none" stroke="#fff" stroke-width="1.2">
          <circle cx="13" cy="13" r="6"/>
          <ellipse cx="13" cy="13" rx="2.6" ry="6"/>
          <line x1="7" y1="13" x2="19" y2="13"/>
        </g>
      </svg>
    </li>
    <li>
      <span class="lines">Unit 7, Foundry Road<br>CA, USA 905310</span>
      <svg class="icon" viewBox="0 0 26 26" aria-hidden="true">
        <rect width="26" height="26" fill="var(--red)"/>
        <path d="M13 6a4.5 4.5 0 0 0-4.5 4.5c0 3.4 4.5 9 4.5 9s4.5-5.6 4.5-9A4.5 4.5 0 0 0 13 6z" fill="#fff"/>
        <circle cx="13" cy="10.5" r="1.7" fill="var(--red)"/>
      </svg>
    </li>
  </ul>
</main>
</body>
</html>
```